Business Card Design for Oncology Consulting Company

We need a business card design using a logo that has already been created.

Company name is: WMBHO - Meridian Centre for Clinical Review and Genetic Guidance

We would also like to include the following pieces of information on the business card:
Name
Title
US Address (street, city, state, zip, country)
Email address
Website address

Target Market(s)

The target customers are physicians (oncologists, pathologists) in Greece, Iran, US, etc who would refer patients to our company for a second medical opinion/genetic counseling for cancer.

Industry/Entity Type

Business

Colors

Designer to choose colors to be used in the design.

Requirements
Must have
• Must contain logo in attached file and elements described above.

```html
<!DOCTYPE html>
<html lang="en">
<head>
<meta charset="utf-8">
<title>WMBHO Business Card</title>
<link rel="stylesheet" href="https://fonts.googleapis.com/css2?family=Ubuntu:wght@400;500;700&display=swap">
<style>
  :root {
    --brand-blue: #1a6cb6;
    --card-white: #ffffff;
    --tagline-grey: #8a9099;
    --canvas-bg: #eceef1;
    --text-on-blue: #ffffff;
    --rule-on-blue: rgba(255,255,255,0.85);
  }
  * { box-sizing: border-box; margin: 0; padding: 0; }
  html, body {
    width: 1200px; height: 1000px; overflow: hidden;
    background: var(--canvas-bg);
    font-family: "Ubuntu", sans-serif;
  }
  .canvas { position: relative; width: 1200px; height: 1000px; }
  .card {
    position: absolute; left: 250px; width: 700px; height: 400px;
    border-radius: 28px; overflow: hidden;
    box-shadow: 0 6px 20px rgba(0,0,0,0.12);
  }

  /* Front */
  .card-front { top: 60px; background: var(--card-white); }
  .front-tagline {
    position: absolute; left: 330px; top: 96px; width: 330px;
    border-top: 2px solid var(--tagline-grey); padding-top: 5px;
    font-size: 10px; font-weight: 500; color: var(--tagline-grey);
    text-transform: uppercase; letter-spacing: 0.4px; white-space: nowrap;
  }
  .front-brand {
    position: absolute; left: 44px; top: 150px;
    display: flex; align-items: center; gap: 18px;
  }
  .front-brand .brand-name {
    font-size: 100px; font-weight: 700; color: var(--brand-blue);
    letter-spacing: 2px; line-height: 1;
  }
  .front-brand .brand-dot {
    width: 20px; height: 20px; border-radius: 50%; background: var(--brand-blue);
  }
  .front-band {
    position: absolute; left: 0; bottom: 0; width: 100%; height: 70px;
    background: var(--brand-blue);
    display: flex; align-items: center; justify-content: center;
  }
  .website { color: var(--text-on-blue); font-size: 22px; letter-spacing: 0.5px; }

  /* Back */
  .card-back { top: 540px; background: var(--brand-blue); color: var(--text-on-blue); }
  .back-tagline {
    position: absolute; left: 330px; top: 52px; width: 340px;
    font-size: 20px; text-transform: uppercase; line-height: 1.25; letter-spacing: 0.3px;
  }
  .back-brand {
    position: absolute; left: 44px; top: 122px;
    font-size: 80px; font-weight: 700; letter-spacing: 2px; line-height: 1;
  }
  .person {
    position: absolute; right: 245px; top: 212px; text-align: right;
  }
  .person-name { font-size: 32px; font-weight: 700; line-height: 1.15; }
  .person-title { font-size: 32px; font-weight: 400; line-height: 1.15; }
  .contact {
    position: absolute; left: 470px; top: 206px;
    border-left: 2px solid var(--rule-on-blue); padding-left: 12px;
    list-style: none; font-size: 20px; line-height: 1.35;
  }
  .contact li { display: flex; align-items: center; gap: 8px; }
  .contact svg { width: 18px; height: 18px; flex: none; }
  .address {
    position: absolute; left: 300px; top: 310px;
    display: flex; align-items: center; gap: 8px; font-size: 22px;
  }
  .address svg { width: 16px; height: 20px; }
</style>
</head>
<body>
<main class="canvas">
  <section class="card card-front" aria-label="Business card front">
    <p class="front-tagline">Meridian Centre for Clinical Review and Genetic Guidance</p>
    <div class="front-brand">
      <span class="brand-name">WMBHO</span>
      <span class="brand-dot"></span>
    </div>
    <div class="front-band">
      <span class="website">www.website address.com</span>
    </div>
  </section>

  <section class="card card-back" aria-label="Business card back">
    <p class="back-tagline">Meridian Centre for Clinical Review and Genetic Guidance</p>
    <div class="back-brand">WMBHO</div>
    <div class="person">
      <p class="person-name">Name here</p>
      <p class="person-title">Title here</p>
    </div>
    <ul class="contact">
      <li>
        <svg viewBox="0 0 18 18" aria-hidden="true"><rect x="5" y="1" width="8" height="16" rx="1.5" fill="none" stroke="#fff" stroke-width="1.4"/><circle cx="9" cy="14.5" r="0.9" fill="#fff"/></svg>
        <span>12345678910</span>
      </li>
      <li>
        <svg viewBox="0 0 18 18" aria-hidden="true"><rect x="2" y="7" width="14" height="9" rx="1" fill="none" stroke="#fff" stroke-width="1.4"/><rect x="5" y="2" width="8" height="5" fill="none" stroke="#fff" stroke-width="1.4"/><line x1="5" y1="11" x2="13" y2="11" stroke="#fff" stroke-width="1.2"/></svg>
        <span>12345678910</span>
      </li>
      <li>
        <svg viewBox="0 0 18 18" aria-hidden="true"><rect x="1.5" y="4" width="15" height="10" fill="none" stroke="#fff" stroke-width="1.4"/><polyline points="1.5,4 9,10 16.5,4" fill="none" stroke="#fff" stroke-width="1.4"/></svg>
        <span>Email address</span>
      </li>
    </ul>
    <p class="address">
      <svg viewBox="0 0 16 20" aria-hidden="true"><path d="M8 1a6 6 0 0 0-6 6c0 4.5 6 12 6 12s6-7.5 6-12a6 6 0 0 0-6-6z" fill="#cfd8e3"/><circle cx="8" cy="7" r="2.2" fill="#1a6cb6"/></svg>
      <span>street, city, state, zip, country</span>
    </p>
  </section>
</main>
</body>
</html>
```